Book Cover Design Project

I have written a booK called "Build From Nothing:
a handbook for launching and steering a modest enterprise. It is aimed at the start up entrepreneur and seeks to give them everything they need to start up and run a small business. I am interested in a very simple cover that is contemporary in the look but clearly communicates the mission of the book. It should sell very well as there are no others like it, so the designer will get excellent exposure.
Updates

Reason: I an vacation in Europe until the 23rd of July. Would like a few days to make a decision after my return Ned

We are currently on vacation.  Will make a final decision in about a week.  Thanks so much for your submissions

Ned

Target Market(s)

Start up businesses in the U.S.

Industry/Entity Type

Business

Requirements
Must have
• Clear communication of the name. Lots of white space. Graphic communication of the purpose of the book? Prominent exposure of my name. Edward r. Kistlewood

```html
<!DOCTYPE html>
<html lang="en">
<head>
<meta charset="utf-8">
<title>Build From Nothing — Book Cover</title>
<link rel="stylesheet" href="https://fonts.googleapis.com/css2?family=Oswald:wght@300;400;500;600&display=swap">
<style>
  :root {
    --page: #ffffff;
    --cover: #ffffff;
    --cover-edge: #1a1a1a;
    --cover-shadow: rgba(0, 0, 0, 0.35);
    --author-blue: #1f5aa8;
    --title-blue: #45b8e8;
    --subtitle-grey: #555a5e;
    --figure-blue: #1f55a6;
    --gear-green: #6cbb45;
    --gear-deep-green: #0f9456;
    --gear-sky: #55c3ef;
    --gear-teal: #1483b8;
    --gear-mist: #eeeeee;
  }
  * { margin: 0; padding: 0; box-sizing: border-box; }
  html, body {
    width: 1200px;
    height: 900px;
    overflow: hidden;
    background: var(--page);
  }
  .canvas {
    position: relative;
    width: 1200px;
    height: 900px;
    background: var(--page);
  }
  .book-cover {
    position: absolute;
    left: 300px;
    top: 5px;
    width: 593px;
    height: 888px;
    background: var(--cover);
    border: 1px solid var(--cover-edge);
    box-shadow: 4px 4px 5px var(--cover-shadow);
    overflow: hidden;
  }
  .author-name {
    position: absolute;
    left: 57px;
    top: 88px;
    font-family: "Oswald", sans-serif;
    font-weight: 600;
    font-size: 36px;
    letter-spacing: 1.5px;
    color: var(--author-blue);
    text-transform: uppercase;
    white-space: nowrap;
  }
  .book-title {
    position: absolute;
    left: 20px;
    top: 163px;
    width: 553px;
    font-family: "Oswald", sans-serif;
    font-weight: 500;
    font-size: 64px;
    line-height: 1;
    letter-spacing: -0.5px;
    color: var(--title-blue);
    text-transform: uppercase;
    white-space: nowrap;
    transform: scaleY(1.3);
    transform-origin: left top;
  }
  .book-subtitle {
    position: absolute;
    left: 57px;
    top: 308px;
    font-family: "Oswald", sans-serif;
    font-weight: 400;
    font-size: 26px;
    line-height: 36px;
    letter-spacing: 0.8px;
    color: var(--subtitle-grey);
    text-transform: uppercase;
    white-space: nowrap;
  }
  .runner-figure {
    position: absolute;
    left: 355px;
    top: 332px;
    width: 170px;
    height: 238px;
    background: var(--figure-blue);
    border-radius: 46% 42% 38% 44% / 30% 34% 46% 40%;
  }
  .gear-field {
    position: absolute;
    left: 0;
    bottom: 0;
    width: 593px;
    height: 390px;
  }
</style>
</head>
<body>
<main class="canvas">
  <section class="book-cover">
    <p class="author-name">Edward R. Kistlewood</p>
    <h1 class="book-title">Build From Nothing</h1>
    <p class="book-subtitle">A handbook for<br>launching and steering<br>a modest enterprise</p>
    <div class="runner-figure" role="img" aria-label="Blue silhouette of a person leaping forward"></div>
    <svg class="gear-field" viewBox="0 0 593 390" role="img" aria-label="Cluster of interlocking green and blue gears rising from the bottom of the cover">
      <defs>
        <linearGradient id="gear-field-fill" x1="0" y1="0" x2="1" y2="1">
          <stop offset="0" stop-color="var(--gear-green)"/>
          <stop offset="0.45" stop-color="var(--gear-deep-green)"/>
          <stop offset="0.75" stop-color="var(--gear-sky)"/>
          <stop offset="1" stop-color="var(--gear-teal)"/>
        </linearGradient>
      </defs>
      <path d="M0 390 L0 170 C40 150 70 120 110 110 C130 60 170 40 215 50 C250 60 260 100 300 110 C330 80 380 70 410 90 C450 90 480 110 520 105 C560 110 580 140 593 160 L593 390 Z" fill="var(--gear-mist)"/>
      <path d="M0 390 L0 190 C40 170 80 160 110 180 C125 130 170 120 200 140 C225 110 280 110 320 140 C350 100 400 110 420 150 C460 120 520 130 560 170 C580 200 593 230 593 250 L593 390 Z" fill="url(#gear-field-fill)"/>
    </svg>
  </section>
</main>
</body>
</html>
```